Book Cover for College Series

We need an e-book cover design for a collection of poetry entitled, "Quiet Ledger Vol. 1: The Heartland." Although the price is set to $200, whomever I select for this project will be used for the next three volumes of the series in the future. So be sure to have contact information ready if selected.
If selected, we can be reached at BrightQuillPress@mailnest.example
Be sure to check out the Look and Feel Slider. We would like it to come across as serious and professional, yet very personable and modern.
Target Market(s)
Target market is both current college students as well as former college students (University alums). However, on some level it is marketed towards anyone associated with universities, including professors, as well as poetry readers. Which is why, although personable, We need the look to have a serious feel to it as well.
Industry/Entity Type
College
Requirements
Must have
- The title of the book: "Quiet Ledger: Vol 1. The Heartland"
- Be sure to have the author's name: Tobias Wendell Marsh
Nice to have
- - Nice to have a design that somehow gives off the feeling of nostalgia.
Optional: Underneath the title, include "A collection of poetry celebrating the top universities of the Midwest."
- Only include the following if it does not get in the way of the feel/look of the cover: Have the initials: T.W.M. on the left-hand corner. An example of how this should appear is in the photo attached However, it does not necessarily need to be this big.

```html
<!DOCTYPE html>
<html lang="en">
<head>
<meta charset="UTF-8">
<title>Quiet Ledger Vol. 1: The Heartland — Cover</title>
<link href="https://fonts.googleapis.com/css2?family=Quicksand:wght@300;400;500;700&display=swap" rel="stylesheet">
<style>
  :root {
    --page-bg: #ececec;
    --ink-light: #ffffff;
    --ink-soft: #f3ece6;
    --sky-night: #231f3d;
    --sky-dusk: #5a3440;
    --sky-ember: #b8521f;
    --sky-glow: #f2951f;
    --sky-sun: #fbb22a;
    --earth-rust: #5a2410;
    --earth-dark: #120905;
    --rule: rgba(255, 255, 255, 0.85);
  }
  * { margin: 0; padding: 0; box-sizing: border-box; }
  html, body {
    width: 1200px;
    height: 1200px;
    overflow: hidden;
    background: var(--page-bg);
  }
  .cover {
    position: absolute;
    left: 227px;
    top: 40px;
    width: 746px;
    height: 1120px;
    overflow: hidden;
    font-family: "Quicksand", sans-serif;
    color: var(--ink-light);
  }
  .cover-photo {
    position: absolute;
    inset: 0;
    background:
      radial-gradient(ellipse 70% 30% at 0% 62%, rgba(251, 178, 42, 0.75), rgba(251, 178, 42, 0) 70%),
      radial-gradient(ellipse 40% 12% at 25% 22%, rgba(230, 110, 80, 0.55), rgba(230, 110, 80, 0) 75%),
      linear-gradient(to bottom,
        var(--sky-night) 0%,
        var(--sky-dusk) 16%,
        var(--sky-ember) 32%,
        var(--sky-glow) 50%,
        var(--sky-ember) 64%,
        var(--earth-rust) 74%,
        var(--earth-dark) 84%,
        var(--earth-dark) 100%);
  }
  .cover-photo::after {
    content: "";
    position: absolute;
    inset: 0;
    background: linear-gradient(to right, rgba(0,0,0,0) 55%, rgba(20,10,25,0.45) 100%);
  }
  .frame {
    position: absolute;
    top: 42px;
    left: 42px;
    right: 42px;
    bottom: 42px;
    border: 1px solid var(--rule);
    border-bottom: none;
  }
  .frame-foot {
    position: absolute;
    left: -1px;
    right: -1px;
    bottom: -8px;
    display: flex;
    align-items: center;
    gap: 10px;
  }
  .frame-foot::before,
  .frame-foot::after {
    content: "";
    flex: 1;
    height: 1px;
    background: var(--rule);
  }
  .tagline {
    font-size: 13px;
    font-weight: 700;
    letter-spacing: 0.01em;
    white-space: nowrap;
    color: var(--ink-soft);
  }
  .title-block {
    position: absolute;
    left: 0;
    right: 0;
    top: 250px;
    text-align: center;
  }
  .series {
    font-size: 22px;
    font-weight: 400;
    letter-spacing: 0.01em;
  }
  .title {
    margin-top: 2px;
    font-size: 55px;
    font-weight: 300;
    letter-spacing: 0.2em;
    line-height: 1.1;
    padding-left: 0.2em;
  }
  .author {
    position: absolute;
    left: 0;
    right: 0;
    top: 1014px;
    text-align: center;
    font-size: 18px;
    font-weight: 400;
    letter-spacing: 0.02em;
    color: var(--ink-soft);
  }
</style>
</head>
<body>
  <main class="cover">
    <div class="cover-photo" role="img" aria-label="Photograph of a sunset sky over a grassy field, with a silhouetted park bench and a distant windmill"></div>
    <div class="frame">
      <div class="frame-foot">
        <p class="tagline">A collection of poetry celebrating the top universities of the Midwest</p>
      </div>
    </div>
    <header class="title-block">
      <p class="series">Quiet Ledger | Vol 1</p>
      <h1 class="title">The Heartland</h1>
    </header>
    <p class="author">Tobias Wendell Marsh</p>
  </main>
</body>
</html>
```